Photoshop Templates for Instagram, x 2

A Square template to reuse that is on brand.

It will involve an image and text of between 3 and 10 words.
I would like 2 separate contrasting images to use interchangeably

In the files I have added some of the images that I have been using, as well as the home page of my website that is currently being developed.

The on brand would be very recognisable with the website.

Requirements
Must have
• Must be similar in feel to the home page.

Must be simple to to change image and and text in the template

I would like 2 designs. Both similar, but contrasting

The square images show the look that I have been using (created by myself, so I'm sure these can be massively improved upon)

```html
<!DOCTYPE html>
<html lang="en">
<head>
<meta charset="utf-8">
<title>PEAKMIND – Instagram Quote Templates</title>
<link rel="stylesheet" href="https://fonts.googleapis.com/css2?family=Open+Sans:wdth,wght@75..100,600..800&family=Oswald:wght@400&display=swap">
<style>
  :root {
    --page-bg: #ececec;
    --card-bg: #0b0b0b;
    --card-glow: #2a2a2a;
    --brand-blue: #3d9fdf;
    --brand-blue-light: #63b6ea;
    --text-white: #ffffff;
  }
  * { margin: 0; padding: 0; box-sizing: border-box; }
  html, body {
    width: 1200px; height: 2353px; overflow: hidden;
    background: var(--page-bg);
  }
  .quote-card {
    position: absolute; left: 40px;
    width: 1120px; height: 1120px;
    overflow: hidden;
    background: radial-gradient(circle at 70% 45%, var(--card-glow) 0%, var(--card-bg) 60%);
    color: var(--text-white);
  }
  .quote-card--first { top: 30px; }
  .quote-card--second { top: 1190px; }
  .photo-bands { position: absolute; inset: 0; width: 1120px; height: 1120px; }
  .quote-line {
    position: absolute;
    font-family: "Open Sans", sans-serif;
    font-weight: 700;
    font-stretch: 88%;
    line-height: 1;
    white-space: nowrap;
    text-align: justify;
    text-align-last: justify;
    text-transform: uppercase;
  }
  .quote-card--first .quote-line { left: 37px; width: 473px; }
  .quote-card--second .quote-line { left: 54px; width: 358px; font-weight: 600; }
  .quote-line--free { text-align-last: left; width: auto !important; }
  .quote-rule {
    position: absolute; height: 3px; background: var(--text-white);
  }
  .quote-card--first .quote-rule { left: 37px; width: 473px; }
  .quote-card--second .quote-rule { left: 54px; width: 358px; }
  .quote-author {
    position: absolute;
    font-family: "Oswald", sans-serif;
    font-weight: 400;
    font-size: 31px;
    letter-spacing: -1px;
    text-transform: uppercase;
    text-align: right;
    line-height: 1;
  }
  .brand-name {
    position: absolute;
    font-family: "Open Sans", sans-serif;
    font-weight: 700;
    font-stretch: 88%;
    font-size: 28px;
    line-height: 1;
    letter-spacing: 0.5px;
    color: var(--text-white);
  }
</style>
</head>
<body>

<section class="quote-card quote-card--first">
  <svg class="photo-bands" viewBox="0 0 1226 1226" role="img" aria-label="Blue-toned photo of a footballer in a club shirt gesturing to his temple, shown through diagonal bands">
    <defs>
      <linearGradient id="bandToneA" x1="0" y1="0" x2="1" y2="1">
        <stop offset="0" stop-color="var(--brand-blue-light)"/>
        <stop offset="1" stop-color="var(--brand-blue)"/>
      </linearGradient>
    </defs>
    <g transform="rotate(-45)" fill="url(#bandToneA)">
      <rect x="290" y="470" width="2000" height="180"/>
      <rect x="200" y="668" width="2000" height="172"/>
      <rect x="110" y="858" width="2000" height="182"/>
      <rect x="20" y="1058" width="2000" height="182"/>
      <rect x="-60" y="1258" width="2000" height="182"/>
      <rect x="-150" y="1458" width="2000" height="182"/>
    </g>
  </svg>

  <p class="quote-line" style="top:159px;font-size:46px;">“If you’re nervous</p>
  <div class="quote-rule" style="top:229px;"></div>
  <p class="quote-line" style="top:250px;font-size:46px;">You think ‘I don’t</p>
  <p class="quote-line" style="top:294px;font-size:56px;">Want to make</p>
  <p class="quote-line" style="top:348px;font-size:46px;">Mistakes or give</p>
  <p class="quote-line" style="top:390px;font-size:56px;">The ball away’.</p>
  <div class="quote-rule" style="top:469px;"></div>
  <p class="quote-line" style="top:490px;font-size:44px;">But you limit your</p>
  <p class="quote-line" style="top:531px;font-size:58px;">Own qualities</p>
  <p class="quote-line quote-line--free" style="top:573px;font-size:148px;">Then”</p>
  <p class="quote-author" style="top:769px;right:610px;">-Marco Veldhuis</p>

  <p class="brand-name" style="left:40px;top:1040px;">PEAKMIND</p>
</section>

<section class="quote-card quote-card--second">
  <svg class="photo-bands" viewBox="0 0 1226 1226" role="img" aria-label="Blue-toned photo of a long-haired footballer running in a club shirt, shown through diagonal bands">
    <defs>
      <linearGradient id="bandToneB" x1="0" y1="0" x2="1" y2="1">
        <stop offset="0" stop-color="var(--brand-blue-light)"/>
        <stop offset="1" stop-color="var(--brand-blue)"/>
      </linearGradient>
    </defs>
    <g transform="rotate(-45)" fill="url(#bandToneB)">
      <rect x="357" y="390" width="2000" height="52"/>
      <rect x="150" y="462" width="2000" height="185"/>
      <rect x="0" y="668" width="2000" height="470"/>
      <rect x="222" y="1160" width="2000" height="170"/>
    </g>
  </svg>

  <p class="quote-line" style="top:112px;font-size:66px;">I was one</p>
  <div class="quote-rule" style="top:200px;"></div>
  <p class="quote-line" style="top:208px;font-size:66px;">Of those</p>
  <div class="quote-rule" style="top:291px;"></div>
  <p class="quote-line" style="top:308px;font-size:50px;">Players who</p>
  <p class="quote-line" style="top:362px;font-size:68px;">Loved to</p>
  <p class="quote-line" style="top:434px;font-size:66px;">Train and</p>
  <div class="quote-rule" style="top:519px;"></div>
  <p class="quote-line" style="top:536px;font-size:68px;">I tried to</p>
  <p class="quote-line" style="top:613px;font-size:54px;">Enjoy every</p>
  <p class="quote-line" style="top:665px;font-size:66px;">Day, every</p>
  <div class="quote-rule" style="top:761px;"></div>
  <p class="quote-line" style="top:770px;font-size:84px;">Session,</p>
  <p class="quote-line" style="top:864px;font-size:56px;">Every game</p>
  <p class="quote-author" style="top:988px;right:610px;">-Andrés Calvo</p>

  <p class="brand-name" style="left:900px;top:1022px;">PEAKMIND</p>
</section>

</body>
</html>
```